Mrs Pellow's Menu Design

Our website is MrsPellows.com.au
Please take inspiration in the look and feel, style and tone from the photos of our takeaway restaurant.

We' have been providing our famous Chinese take away in Merrylands for over 30 years. We have seen the neighbourhood grow around us and we have grown along with them.
We have had a recent shopfitting (see photos on http://www.mrspellows.com.au).

Red features prominently in our shop design but understand if you would keep it muted or minimal for readability.

We would like to revamp our plain menu to a fresh new look with a typeface that emphasizes familiarity and simple, delicious food.
Updates

Reason: Updated brief with more information Would like more designs

Target Market(s)

Our customers are locals who have enjoyed our famous Chinese takeaway for over 30 years. They are mums buying takeout for their family dinner, staff from the surrounding mall shops after a quick, delicious feed and regulars who come in every week for their fix of freshly prepared, familiar Chinese favourites like san choy bow, crispy salt and pepper squid and stir-fried beef in black bean sauce.

Industry/Entity Type

Shop

Requirements
Must have
• Typeface is very important.
It must be readable and convey a classic Chinese menu that oozes familiarity and sincerity. We serve simple, classic Chinese favorites at a economical price
Should not have
• Should not be childish, cartoony or cliched.

```html
<!DOCTYPE html>
<html lang="en">
<head>
<meta charset="utf-8">
<title>Mrs Pellow's Chinese Kitchen – Menu</title>
<link href="https://fonts.googleapis.com/css2?family=Arimo:ital,wght@0,400;0,700;1,400&family=Tinos:wght@400;700&display=swap" rel="stylesheet">
<style>
:root{
  --bg-deep:#1e0202;
  --bg-mid:#4a0606;
  --bg-glow:#7a0c0c;
  --frame:#c9862a;
  --text:#ffffff;
  --text-soft:#f1e6e6;
}
*{box-sizing:border-box;margin:0;padding:0}
html,body{width:1200px;height:900px;overflow:hidden;background:var(--bg-deep)}
.menu{
  position:relative;width:1200px;height:900px;overflow:hidden;
  border:4px solid var(--frame);
  background:
    radial-gradient(ellipse 420px 260px at 250px 180px,rgba(170,20,20,.45),transparent 70%),
    radial-gradient(ellipse 380px 300px at 780px 380px,rgba(170,20,20,.4),transparent 70%),
    radial-gradient(ellipse 300px 200px at 1050px 720px,rgba(150,15,15,.35),transparent 70%),
    linear-gradient(90deg,var(--bg-deep),var(--bg-mid) 30%,var(--bg-glow) 55%,var(--bg-mid) 80%,var(--bg-deep));
  color:var(--text);font-family:"Arimo",Arial,sans-serif;
}
.col{position:absolute}
.col-left{left:3px;top:8px;width:357px}
.col-mid{left:427px;top:12px;width:358px}
.col-right{left:860px;top:0;width:336px;text-align:center}
.section-title{font-family:"Tinos","Times New Roman",serif;font-weight:700;font-size:21px;line-height:24px;margin-top:8px}
.section-title:first-child{margin-top:0}
.section-title small{font-size:14px}
.items{list-style:none}
.item{display:flex;align-items:baseline;font-size:12.6px;line-height:17.6px;height:17.6px;white-space:nowrap}
.item .leader{flex:1;border-bottom:1px dotted var(--text-soft);margin:0 3px;opacity:.8;transform:translateY(-3px)}
.note{font-size:12.6px;line-height:17.6px;padding-left:22px}
.col-mid .section-title{text-align:center;font-weight:400;font-size:21px;line-height:26px}
.col-mid .item{line-height:19.3px;height:19.3px}
.served{font-style:italic;font-size:12.6px;text-align:center;margin-top:12px}
.map{position:absolute;left:430px;top:496px;width:356px;height:212px;background:linear-gradient(180deg,rgba(255,255,255,.10),rgba(255,255,255,.04));border:1px solid rgba(255,255,255,.35)}
.fine-print{position:absolute;left:430px;top:826px;width:356px;text-align:center;font-style:italic;font-size:13px;line-height:19px}
.brand{font-family:"Tinos","Times New Roman",serif;font-weight:700;line-height:1;margin-top:34px}
.brand .l1{display:block;font-size:40px}
.brand .l2{display:block;font-size:31px;margin-top:2px}
.since{font-size:11px;font-weight:700;margin-top:16px;letter-spacing:.5px}
.emblem{display:block;width:220px;height:356px;margin:22px auto 0;background:radial-gradient(ellipse at 50% 45%,rgba(255,255,255,.12),rgba(255,255,255,.02) 70%);border-radius:40px}
.address{font-size:18.5px;line-height:27px;margin-top:22px}
.phone{font-weight:700;font-size:28px;margin-top:24px}
.orders{font-size:16px;line-height:27px;margin-top:12px}
.open{font-weight:700;font-size:22px;margin-top:30px}
.hours{font-weight:700;font-size:16px;margin-top:8px}
</style>
</head>
<body>
<main class="menu">
  <section class="col col-left">
    <h2 class="section-title">Omelette</h2>
    <ul class="items">
      <li class="item">Plain Omelette<span class="leader"></span>$6.90</li>
      <li class="item">Prawn Omelette<span class="leader"></span>$8.00</li>
      <li class="item">Chicken Omelette<span class="leader"></span>$8.00</li>
      <li class="item">Combination Omelette<span class="leader"></span>$8.00</li>
      <li class="item">Vegetable Omelette<span class="leader"></span>$8.00</li>
      <li class="item">BBQ Pork Omelette<span class="leader"></span>$8.00</li>
      <li class="item">Beef Omelette<span class="leader"></span>$9.00</li>
      <li class="item">King Prawn Omelette<span class="leader"></span>$9.50</li>
    </ul>
    <h2 class="section-title">Chow Mein <small>(Served with Crispy Noodles)</small></h2>
    <ul class="items">
      <li class="item">Stir Fried Mixed Vegetable Chow Mein<span class="leader"></span>$7.50</li>
      <li class="item">Prawn Chow Mein<span class="leader"></span>$8.00</li>
      <li class="item">Chicken Chow Mein<span class="leader"></span>$8.00</li>
      <li class="item">Beef Chow Mein<span class="leader"></span>$9.30</li>
      <li class="item">Braised Chicken Chow Mein<span class="leader"></span>$9.30</li>
      <li class="item">Sliced Pork Chow Mein<span class="leader"></span>$9.30</li>
      <li class="item">Combination Chow Mein<span class="leader"></span>$9.80</li>
      <li class="item">King Prawn Chow Mein<span class="leader"></span>$10.40</li>
      <li class="item">Seafood Chow Mein<span class="leader"></span>$12.00</li>
    </ul>
    <p class="note">(Soft Noodles or Thick Rice Noodles at $1.50 extra)</p>
    <h2 class="section-title">Rice</h2>
    <ul class="items">
      <li class="item">Small Fried Rice<span class="leader"></span>$5.00</li>
      <li class="item">Large Fried Rice<span class="leader"></span>$6.00</li>
      <li class="item">Vegetarian Fried Rice<span class="leader"></span>$6.00</li>
      <li class="item">Chicken Fried Rice<span class="leader"></span>$7.50</li>
      <li class="item">Curried Prawns and Rice<span class="leader"></span>$8.00</li>
      <li class="item">Curried Chicken and Rice<span class="leader"></span>$8.00</li>
      <li class="item">Special Fried Rice<span class="leader"></span>$8.50</li>
      <li class="item">Boiled Rice<span class="leader"></span>Small &nbsp;$2.50 ... Large &nbsp;$3.00</li>
    </ul>
    <h2 class="section-title">Thick Rice Noodles</h2>
    <ul class="items">
      <li class="item">Soya Sauce Beef with Thick Rice Noodles<span class="leader"></span>$10.00</li>
      <li class="item">Beef in Scrambled Egg with Thick Rice Noodles<span class="leader"></span>$10.30</li>
      <li class="item">Beef &amp; Black Bean Sauce with Thick Rice Noodles<span class="leader"></span>$10.30</li>
      <li class="item">Braised Chicken with Thick Rice Noodles<span class="leader"></span>$10.30</li>
      <li class="item">Beef and Vegetables with Thick Rice Noodles<span class="leader"></span>$10.30</li>
      <li class="item">Combination Thick Rice Noodles<span class="leader"></span>$11.30</li>
      <li class="item">Sate Chicken with Thick Rice Noodles<span class="leader"></span>$11.40</li>
      <li class="item" style="font-size:11.8px">King Prawn in Scrambled Egg with Thick Rice Noodles<span class="leader"></span>$11.40</li>
      <li class="item" style="font-size:11.2px">Lamb and Black Pepper Sauce with Thick Rice Noodles<span class="leader"></span>$12.30</li>
    </ul>
    <h2 class="section-title">Laksa</h2>
    <ul class="items">
      <li class="item">Vegetable Laksa<span class="leader"></span>$9.50</li>
      <li class="item">Beef Laksa<span class="leader"></span>$10.00</li>
      <li class="item">Braised Chicken Laksa<span class="leader"></span>$10.00</li>
      <li class="item">Combination Laksa<span class="leader"></span>$10.00</li>
      <li class="item">King Prawn Laksa<span class="leader"></span>$10.80</li>
      <li class="item">Seafood Laksa<span class="leader"></span>$12.00</li>
    </ul>
  </section>

  <section class="col col-mid">
    <h2 class="section-title">Lunch Special &nbsp;(10am-3pm)</h2>
    <ul class="items">
      <li class="item">Small Prawns &amp; Vegetables<span class="leader"></span>$6.00</li>
      <li class="item">Curry Prawns<span class="leader"></span>$6.00</li>
      <li class="item">Sweet &amp; Sour Chicken<span class="leader"></span>$6.00</li>
      <li class="item">Chicken &amp; Vegetables<span class="leader"></span>$6.00</li>
      <li class="item">Curry Chicken<span class="leader"></span>$6.00</li>
      <li class="item">Sweet &amp; Sour Pork<span class="leader"></span>$6.00</li>
      <li class="item">Mixed Vegetables<span class="leader"></span>$6.00</li>
      <li class="item">Honey King Prawns<span class="leader"></span>$6.50</li>
      <li class="item">Beef with Black Bean Sauce<span class="leader"></span>$6.50</li>
      <li class="item">Honey Chicken (Boneless)<span class="leader"></span>$6.50</li>
      <li class="item">Lemon Chicken (Boneless)<span class="leader"></span>$6.50</li>
      <li class="item">Deep Fried Lamb with Special Sauce<span class="leader"></span>$6.50</li>
      <li class="item">Mongolian Beef<span class="leader"></span>$7.30</li>
      <li class="item">Beef with Sate Sauce<span class="leader"></span>$7.30</li>
      <li class="item">Beef with Chilli Sauce<span class="leader"></span>$7.30</li>
      <li class="item">Braised Chicken with Sate Sauce<span class="leader"></span>$7.30</li>
      <li class="item">Braised Chicken with Chilli Sauce<span class="leader"></span>$7.30</li>
      <li class="item">Mongolian Lamb<span class="leader"></span>$7.30</li>
    </ul>
    <p class="served">All dishes served with: Boiled Rice or Fried Rice</p>
  </section>

  <div class="map" role="img" aria-label="Street map showing the shop location inside the mall, with mall entries and parking"></div>

  <p class="fine-print">All Prices GST inclusive<br>Prices subject to change without notice<br>All meals contain small quantities of MSG</p>

  <section class="col col-right">
    <h1 class="brand"><span class="l1">MRS. PELLOW'S</span><span class="l2">CHINESE KITCHEN</span></h1>
    <p class="since">SINCE 1976</p>
    <div class="emblem" role="img" aria-label="Line illustration of a guardian lion resting a paw on a ball"></div>
    <p class="address">SHOP 1097 PARKVIEW MALL<br>MERRYLANDS<br>(On Harlow Street,<br>Opp. Council Car Park)</p>
    <p class="phone">Telephone: 9612 3480</p>
    <p class="orders">(Phone Orders Welcome)<br>www.mrspellows.com.au</p>
    <p class="open">OPEN 7 DAYS</p>
    <p class="hours">10.00AM TO 9.00PM</p>
  </section>
</main>
</body>
</html>
```